Harborline Energy - needs a business card

Harborline Energy is a U.S. based diesel sourcing and distribution company that supports American oil & gas fields through providing quality product and consistent services.

Target Market(s)

Oil and Gas

Contact Information for Business Card

The background of the card must be white to ensure the logo pops.

Font styles to use
Serif
Sans Serif

Colors

Designer to choose colors to be used in the design.

Requirements
Must have
• Front of Card: Tag line: Harborline Energy, Powering America's Oil & Gas fields.
• Not sure if you guys do this part but just in case...
• Dale Menschow
• Owner/CEO
• C:555.318.4076
• E:Dmenschow@harborlineenergy.example
• W:Harborlineenergy.example
• Locations: Servicing the Powder River, DJ basin and Bakken formations.
• Back of Card: " Frac fueling is what we do. We understand how important diesel fuel is to your operation, which is why our main service line is Frac fueling. We assure our supply and stand by our service"

```html
<!DOCTYPE html>
<html lang="en">
<head>
<meta charset="utf-8">
<title>Harborline Energy – Business Card</title>
<link rel="stylesheet" href="https://fonts.googleapis.com/css2?family=Roboto:wght@400;500;700&display=swap">
<style>
:root{
  --navy:#1d2f6b;
  --navy-deep:#16255a;
  --red:#c8202f;
  --white:#ffffff;
  --backdrop:#dcdcdc;
}
*{box-sizing:border-box;margin:0;padding:0}
html,body{width:1200px;height:801px;overflow:hidden}
body{background:var(--backdrop);font-family:"Roboto",Arial,sans-serif;position:relative}
.card{position:absolute;top:252px;width:520px;height:297px;background:var(--white);overflow:hidden;box-shadow:0 6px 18px rgba(0,0,0,.18)}
.card--front{left:60px}
.card--back{left:620px}

/* brand lockup */
.brand{display:flex;align-items:center;gap:10px;color:var(--navy);font-weight:700;text-transform:uppercase;letter-spacing:.06em}
.brand__mark{width:34px;height:34px;border-radius:50%;background:var(--red);flex:none}
.card--front .brand{position:absolute;left:0;right:0;top:95px;justify-content:center;font-size:30px}
.card--front .brand__mark{width:44px;height:44px}

.tagline-band{position:absolute;left:0;right:0;bottom:0;height:56px;background:var(--navy);display:flex;align-items:center;justify-content:center}
.tagline{color:var(--white);font-weight:700;font-size:12.5px;letter-spacing:.12em;text-transform:uppercase}

/* back */
.card--back .brand{position:absolute;top:22px;right:24px;font-size:12px}
.card--back .brand__mark{width:18px;height:18px}
.person{position:absolute;top:62px;right:24px;text-align:right}
.person__name{color:var(--red);font-weight:700;font-size:19px;text-transform:uppercase;letter-spacing:.02em}
.person__title{color:var(--navy);font-weight:500;font-size:10px;text-transform:uppercase;letter-spacing:.1em;margin-top:3px}

.info-band{position:absolute;left:0;right:0;top:130px;bottom:0}
.info-band svg{display:block}
.illustration{position:absolute;left:0;top:28px;width:210px;height:210px;background:linear-gradient(135deg,var(--red) 0%,var(--red) 38%,var(--white) 38%,var(--white) 44%,var(--navy) 44%,var(--navy-deep) 100%)}

.locations{position:absolute;right:24px;top:150px;width:230px;text-align:right;color:var(--white);font-size:10.5px;line-height:1.45;letter-spacing:.03em}
.locations__web{color:var(--red);font-weight:500;margin-top:6px;display:block}

.contact{position:absolute;left:222px;bottom:22px;list-style:none;color:var(--white);font-size:10.5px;letter-spacing:.04em}
.contact li{display:flex;align-items:center;gap:8px;margin-top:6px}
.contact svg{width:11px;height:11px;flex:none}
</style>
</head>
<body>

<section class="card card--front" aria-label="Card front">
  <div class="brand"><span class="brand__mark"></span>Harborline Energy</div>
  <div class="tagline-band">
    <p class="tagline">Harborline Energy, Powering America's Oil &amp; Gas fields.</p>
  </div>
</section>

<section class="card card--back" aria-label="Card back">
  <div class="brand"><span class="brand__mark"></span>Harborline Energy</div>
  <div class="person">
    <p class="person__name">Dale Menschow</p>
    <p class="person__title">Owner &amp; CEO</p>
  </div>

  <div class="info-band">
    <svg width="520" height="167" viewBox="0 0 520 167" aria-hidden="true">
      <polygon points="0,60 520,0 520,167 0,167" fill="var(--navy)"/>
    </svg>
  </div>

  <div class="illustration" role="img" aria-label="Large eagle head illustration in red, white and navy"></div>

  <p class="locations">Servicing the Powder River,<br>DJ basin and Bakken formations
    <span class="locations__web">www.harborlineenergy.example</span></p>

  <ul class="contact">
    <li>
      <svg viewBox="0 0 24 24" aria-hidden="true"><path fill="var(--red)" d="M6.6 10.8a15 15 0 0 0 6.6 6.6l2.2-2.2a1 1 0 0 1 1-.25 11.4 11.4 0 0 0 3.6.57 1 1 0 0 1 1 1V20a1 1 0 0 1-1 1A17 17 0 0 1 3 4a1 1 0 0 1 1-1h3.5a1 1 0 0 1 1 1c0 1.25.2 2.45.57 3.57a1 1 0 0 1-.25 1z"/></svg>
      555.318.4076
    </li>
    <li>
      <svg viewBox="0 0 24 24" aria-hidden="true"><rect x="2" y="5" width="20" height="14" fill="none" stroke="var(--red)" stroke-width="2.4"/><path d="M2 5l10 8 10-8" fill="none" stroke="var(--red)" stroke-width="2.4"/></svg>
      Dmenschow@harborlineenergy.example
    </li>
  </ul>
</section>

</body>
</html>
```